Brisk Mend's Blow Their Mind Website

We own a group of cell phone and tablet repair shops in the bay area that is emerging into the mobile device insurance industry and want to develop a site that is clean, organized, and efficient at communicating who we are, the services we provide and the positive feedback we have been getting from our clients. As we enter into this new field of business, Our goal is to attract larger corporate accounts.

We want our home screen to have a big focus on the protection plan for the devices right away much like the home screen from these links:

http://www.gadgetvault.com/

and also - https://us.keepitsnug.com/smartphone-protection.html

We also need to make our repair services clear, here is a website of a company that does repair and we want to highlight both ends of the business.

ww.fixnovo.com

So the home screen will include the tab categories at the top of the screen
home/ protection /repair /about /contact

The first portion will be protection and as you scroll down there will be the next section about repair and following that will be information about the company.

Target Market(s)

Individuals that would be looking for pricing, clients that come to our store, but ultimately the heavy hitters we would want to attract would be larger corporate accounts so the message we want to communicate is professional, organized and credible in the services we provide.

Industry/Entity Type

Cell Phone

Number of Pages Required

5+ page

Font styles to use
Serif

Colors
34a6d7

Requirements
Must have
• Eye catching, organized, with the wow factor that a business will look at our site and will be able to tell that we know what looks good and what grabs peoples attention. A large emphasis on the protection plan section like the links we provided and an organized home screen with the sections highlighted in the project description
• Tabs with links to different sections of the business such as protection that will go into detail about our protections plans and why our plan is best
• repair with a menu of the different prices we provide for different devices and services for that device
• an about us tab
• a contact us tab
Nice to have
• Artistic flow on the homescreen that the different sections flow together without looking too cookie cutter
• Wow factor
Should not have
• Clutter, confusion, disorganization, cheesy cookie cutter

```html
<!DOCTYPE html>
<html lang="en">
<head>
<meta charset="utf-8">
<title>Brisk Mend – Smart Phone Protection Plan</title>
<link href="https://fonts.googleapis.com/css2?family=Source+Sans+3:wght@400;600;700;900&display=swap" rel="stylesheet">
<style>
  :root {
    --brand: #34a6d7;
    --ink: #2b2b2b;
    --muted: #8a8a8a;
    --hero-top: #f6f6f6;
    --hero-bottom: #e1e1e1;
    --shield-dark: #333638;
    --band-top: #1f2d36;
    --band-bottom: #0e171d;
    --footer: #2e2e2e;
    --white: #ffffff;
  }
  * { margin: 0; padding: 0; box-sizing: border-box; }
  html, body { width: 703px; height: 1200px; overflow: hidden; background: var(--white); }
  body { font-family: "Source Sans 3", Arial, sans-serif; color: var(--ink); }
  .page { position: relative; width: 703px; height: 1200px; overflow: hidden; }

  /* Header + hero */
  .hero { position: absolute; left: 0; top: 0; width: 703px; height: 363px;
    background: linear-gradient(180deg, var(--hero-top), var(--hero-bottom)); }
  .brand { position: absolute; left: 34px; top: 22px; display: flex; align-items: center; gap: 7px;
    font-size: 17px; font-weight: 600; color: var(--brand); }
  .brand-mark { width: 14px; height: 14px; background: var(--brand); }
  .nav { position: absolute; right: 40px; top: 27px; display: flex; gap: 6px;
    font-size: 10px; letter-spacing: .5px; color: var(--muted); text-transform: uppercase; }
  .nav a { color: var(--muted); text-decoration: none; }
  .nav a.active { color: var(--brand); border-bottom: 1px solid var(--brand); }
  .hero-title { position: absolute; left: 130px; top: 152px; width: 260px; text-align: center;
    font-size: 29px; line-height: 31px; font-weight: 900; color: var(--brand); text-transform: uppercase; }
  .hero-btn { position: absolute; left: 226px; top: 210px; width: 62px; height: 18px; background: #3a3a3a;
    color: var(--white); font-size: 7px; letter-spacing: .5px; text-align: center; line-height: 18px; text-transform: uppercase; }
  .hero-visual { position: absolute; left: 385px; top: 60px; width: 318px; height: 290px;
    background: radial-gradient(ellipse at 45% 60%, #7a1a1a 0%, #2a2a2a 35%, #bfc4c7 70%, rgba(225,225,225,0) 100%); }
  .slider-dots { position: absolute; left: 322px; top: 331px; display: flex; gap: 5px; }
  .slider-dots span { width: 14px; height: 4px; background: #3a3a3a; }
  .slider-dots span.on { background: var(--brand); }

  /* Features */
  .features { position: absolute; left: 0; top: 363px; width: 703px; height: 305px; background: var(--white); }
  .features svg.links { position: absolute; left: 0; top: 0; }
  .shield { position: absolute; }
  .shield span { position: absolute; left: 0; width: 100%; text-align: center; color: var(--white);
    font-weight: 700; text-transform: uppercase; }
  .shield-small span { top: 14px; font-size: 8px; letter-spacing: .3px; }
  .shield-main span.title { top: 42px; font-size: 23px; font-weight: 700; }
  .shield-main p { position: absolute; left: 20px; top: 76px; width: 100px; font-size: 6px; line-height: 8px;
    color: var(--white); text-align: center; }

  /* Difference band */
  .difference { position: absolute; left: 0; top: 668px; width: 703px; height: 253px;
    background: linear-gradient(180deg, var(--band-top), var(--band-bottom)); color: var(--white); }
  .section-title { position: absolute; left: 0; width: 703px; text-align: center; font-size: 23px;
    font-weight: 700; color: var(--brand); text-transform: uppercase; }
  .difference .section-title { top: 32px; }
  .stat { position: absolute; top: 92px; width: 170px; text-align: center; }
  .stat svg { display: block; margin: 0 auto 10px; }
  .stat small { display: block; font-size: 9px; letter-spacing: .3px; text-transform: uppercase; color: #dfe6ea; }
  .stat strong { display: block; font-size: 27px; font-weight: 700; text-transform: uppercase; line-height: 30px; }
  .divider { position: absolute; top: 86px; width: 1px; height: 120px; background: #5b6870; }

  /* Customers */
  .customers { position: absolute; left: 0; top: 921px; width: 703px; height: 244px; background: var(--white); }
  .customers .section-title { top: 36px; }
  .client { position: absolute; width: 88px; margin-left: -44px; text-align: center;
    font-size: 15px; font-weight: 700; color: #3a3a3a; }

  /* Footer */
  .footer { position: absolute; left: 0; top: 1165px; width: 703px; height: 35px; background: var(--footer);
    color: #9a9a9a; font-size: 8px; }
  .footer .copy { position: absolute; left: 88px; top: 13px; }
  .footer .copy b { color: var(--brand); font-weight: 400; }
  .footer .find { position: absolute; right: 80px; top: 12px; display: flex; align-items: center; gap: 8px; }
  .footer .find i { width: 8px; height: 8px; background: #9a9a9a; display: inline-block; }
</style>
</head>
<body>
<div class="page">

  <header class="hero">
    <div class="brand"><span class="brand-mark"></span>Brisk Mend</div>
    <nav class="nav">
      <a class="active" href="#">Home</a><span>/</span>
      <a href="#">Protection</a><span>/</span>
      <a href="#">Repair</a><span>/</span>
      <a href="#">About</a><span>/</span>
      <a href="#">Contact</a>
    </nav>
    <h1 class="hero-title">Smart Phone Protection Plan</h1>
    <div class="hero-btn">Read more</div>
    <div class="hero-visual" role="img" aria-label="Smartphone with a stethoscope wrapped around it over a water splash"></div>
    <div class="slider-dots"><span class="on"></span><span></span><span></span></div>
  </header>

  <section class="features">
    <svg class="links" width="703" height="305" viewBox="0 0 703 305" fill="none" stroke="#d6d6d6" stroke-width="1">
      <path d="M178 95 C 220 95, 250 110, 282 125"/>
      <path d="M525 95 C 483 95, 453 110, 421 125"/>
      <path d="M198 230 C 230 225, 255 205, 282 190"/>
      <path d="M505 230 C 473 225, 448 205, 421 190"/>
    </svg>

    <div class="shield shield-small" style="left:122px; top:68px; width:56px; height:64px;">
      <svg width="56" height="64" viewBox="0 0 56 64"><path d="M28 0 L56 8 V30 C56 48 42 58 28 64 C14 58 0 48 0 30 V8 Z" fill="var(--shield-dark)"/></svg>
      <span>Insurance</span>
    </div>
    <div class="shield shield-small" style="left:525px; top:68px; width:56px; height:64px;">
      <svg width="56" height="64" viewBox="0 0 56 64"><path d="M28 0 L56 8 V30 C56 48 42 58 28 64 C14 58 0 48 0 30 V8 Z" fill="var(--shield-dark)"/></svg>
      <span>Tablet</span>
    </div>
    <div class="shield shield-small" style="left:142px; top:198px; width:56px; height:64px;">
      <svg width="56" height="64" viewBox="0 0 56 64"><path d="M28 0 L56 8 V30 C56 48 42 58 28 64 C14 58 0 48 0 30 V8 Z" fill="var(--shield-dark)"/></svg>
      <span>Repairing</span>
    </div>
    <div class="shield shield-small" style="left:505px; top:198px; width:56px; height:64px;">
      <svg width="56" height="64" viewBox="0 0 56 64"><path d="M28 0 L56 8 V30 C56 48 42 58 28 64 C14 58 0 48 0 30 V8 Z" fill="var(--shield-dark)"/></svg>
      <span>Phone</span>
    </div>

    <div class="shield shield-main" style="left:281px; top:70px; width:141px; height:166px;">
      <svg width="141" height="166" viewBox="0 0 141 166"><path d="M70.5 0 L141 18 V74 C141 122 106 148 70.5 166 C35 148 0 122 0 74 V18 Z" fill="var(--brand)"/></svg>
      <span class="title">Features</span>
      <p>Fast repairs, fair plans and full cover for every phone and tablet you rely on daily.</p>
    </div>
  </section>

  <section class="difference">
    <h2 class="section-title">What makes us different?</h2>

    <div class="stat" style="left:85px;">
      <svg width="34" height="30" viewBox="0 0 34 30" fill="none" stroke="var(--brand)" stroke-width="2.5">
        <path d="M1 3 H7 L11 20 H28 L32 8 H9"/>
        <circle cx="13" cy="26" r="2.5" fill="var(--brand)"/>
        <circle cx="26" cy="26" r="2.5" fill="var(--brand)"/>
      </svg>
      <small>Buy online in less than</small>
      <strong>2 Minutes</strong>
    </div>
    <div class="divider" style="left:262px;"></div>
    <div class="stat" style="left:267px;">
      <svg width="30" height="30" viewBox="0 0 30 30">
        <circle cx="15" cy="15" r="14" fill="var(--brand)"/>
        <text x="15" y="18" text-anchor="middle" font-family="Source Sans 3, Arial, sans-serif" font-size="8" font-weight="700" fill="#fff">SOLD</text>
      </svg>
      <small>We've sold more than</small>
      <strong>1 Million</strong>
    </div>
    <div class="divider" style="left:445px;"></div>
    <div class="stat" style="left:446px;">
      <svg width="30" height="30" viewBox="0 0 30 30">
        <circle cx="15" cy="15" r="14" fill="var(--brand)"/>
        <text x="15" y="18" text-anchor="middle" font-family="Source Sans 3, Arial, sans-serif" font-size="8" font-weight="700" fill="#fff">SOLD</text>
      </svg>
      <small>We're backed by a</small>
      <strong>Fortune</strong>
    </div>
  </section>

  <section class="customers">
    <h2 class="section-title">Thousands of happy customers</h2>
    <div class="client" style="left:129px; top:92px;">Norvale</div>
    <div class="client" style="left:216px; top:92px;">Quillon</div>
    <div class="client" style="left:305px; top:92px;">Fenwright</div>
    <div class="client" style="left:391px; top:92px;">Ardell</div>
    <div class="client" style="left:480px; top:92px;">Sonari</div>
    <div class="client" style="left:574px; top:92px;">Hexmont</div>
    <div class="client" style="left:129px; top:162px;">Introva</div>
    <div class="client" style="left:216px; top:162px;">Westbury</div>
    <div class="client" style="left:305px; top:162px;">Ninefold</div>
    <div class="client" style="left:391px; top:162px;">Lavelle</div>
    <div class="client" style="left:480px; top:162px;">Amberly</div>
    <div class="client" style="left:574px; top:162px;">Castlow</div>
  </section>

  <footer class="footer">
    <div class="copy">Copyright © 2015 <b>Brisk Mend</b> | All Rights Reserved</div>
    <div class="find">Find us: <i></i><i></i></div>
  </footer>

</div>
</body>
</html>
```